R.T.Pell Logging Web design

Our website needs a redesign. We want it to appear professional and easy to navigate. We will be adding videos and pictures to the new website. We do not sell any products on our website. It should be designed for informational purposes. Our company performs timber harvesting and forest management services. Attached is our new company logo.

www.rtpelllogging-example.com if you want to see our current website.

Industry/Entity Type

Graphic Design

Coding

Coded - Design and coding required

```html
<!DOCTYPE html>
<html lang="en">
<head>
<meta charset="utf-8">
<title>R.T. Pell Logging Company</title>
<link href="https://fonts.googleapis.com/css2?family=Lato:ital,wght@0,400;0,700;0,900;1,700&display=swap" rel="stylesheet">
<style>
:root{
  --brown:#6b3510;
  --brown-dark:#5a2c0c;
  --gold:#e3ac42;
  --gold-light:#e8b957;
  --wood:#d9b98f;
  --wood-dark:#c9a173;
  --white:#ffffff;
  --text:#4a2a12;
}
*{margin:0;padding:0;box-sizing:border-box}
html,body{width:1200px;height:1197px;overflow:hidden}
body{
  font-family:'Lato',sans-serif;
  background:linear-gradient(90deg,var(--wood) 0%,var(--wood-dark) 50%,var(--wood) 100%);
  position:relative;color:var(--text);
}
.page{position:absolute;left:132px;top:32px;width:936px;height:1118px;background:var(--white);border-top:6px solid var(--brown);border-bottom:7px solid var(--brown)}
.header{position:absolute;left:0;top:0;width:936px;height:108px}
.brand{position:absolute;left:28px;top:28px;display:flex;align-items:center;gap:14px}
.brand-mark{width:50px;height:50px;background:var(--gold)}
.brand-name{font-weight:900;font-size:34px;line-height:1;color:var(--brown);letter-spacing:1px}
.brand-sub{font-weight:400;font-size:16px;letter-spacing:5px;color:var(--brown);margin-top:4px}
.phone{position:absolute;right:24px;top:38px;display:flex;align-items:center;gap:8px;font-weight:700;font-size:25px;color:var(--brown)}
.nav{position:absolute;left:0;top:108px;width:936px;height:50px;display:flex;background:linear-gradient(#e6b24a,#d9a033)}
.nav a{display:flex;align-items:center;justify-content:center;height:50px;color:var(--brown);text-decoration:none;font-size:18px;border-right:1px solid #c98f2a}
.nav a:last-child{border-right:0}
.nav a.active{background:var(--brown);color:var(--gold)}
.hero{position:absolute;left:0;top:158px;width:936px;height:510px;background:linear-gradient(180deg,#3e4a25 0%,#6a5a28 45%,#b8862e 70%,#3a3d1d 100%)}
.card{position:absolute;top:517px;width:280px;height:211px}
.card-photo{height:151px}
.card-label{height:60px;background:var(--brown);display:flex;align-items:center;justify-content:space-between;padding:0 12px 0 8px;color:var(--gold);font-weight:700;font-size:20px}
.arrow{width:26px;height:26px;border-radius:50%;background:var(--gold);display:flex;align-items:center;justify-content:center}
.section-title{position:absolute;font-weight:700;font-size:19px;color:var(--brown)}
.rule{position:absolute;height:4px}
.rule::before{content:"";position:absolute;left:0;top:0;width:66px;height:4px;background:var(--gold)}
.rule::after{content:"";position:absolute;left:66px;top:1px;right:0;height:1px;background:var(--brown)}
.intro{position:absolute;left:26px;top:1007px;width:581px;font-size:12.5px;line-height:17.6px;text-align:justify}
.intro p{margin-bottom:17.6px}
.video{position:absolute;left:632px;top:809px;width:280px;height:179px;background:linear-gradient(135deg,#6f7258,#8a7f4f 50%,#a49a80);display:flex;align-items:center;justify-content:center}
.footer{position:absolute;left:0;top:1019px;width:936px;height:85px;background:var(--gold)}
.footer-links{position:absolute;left:24px;top:15px;font-weight:700;font-size:11.5px;color:var(--brown)}
.footer-links span{margin:0 9px;font-weight:400}
.copyright{position:absolute;left:24px;top:52px;font-weight:700;font-size:11.5px;color:var(--brown)}
.follow{position:absolute;right:24px;top:47px;display:flex;align-items:center;gap:4px;font-weight:700;font-style:italic;font-size:11.5px;color:var(--brown)}
.follow i{display:block;width:28px;height:28px;border-radius:50%;background:var(--brown);margin-left:3px}
</style>
</head>
<body>
<div class="page">
  <header class="header">
    <div class="brand">
      <div class="brand-mark"></div>
      <div>
        <div class="brand-name">R.T. PELL</div>
        <div class="brand-sub">LOGGING COMPANY</div>
      </div>
    </div>
    <div class="phone">
      <svg width="24" height="24" viewBox="0 0 24 24"><path fill="#e3ac42" d="M6.6 10.8c1.4 2.8 3.8 5.1 6.6 6.6l2.2-2.2c.3-.3.7-.4 1-.2 1.1.4 2.3.6 3.6.6.6 0 1 .4 1 1V20c0 .6-.4 1-1 1C10.6 21 3 13.4 3 4c0-.6.4-1 1-1h3.5c.6 0 1 .4 1 1 0 1.3.2 2.5.6 3.6.1.3 0 .7-.2 1z"/></svg>
      (555) 014-2287
    </div>
  </header>
  <nav class="nav">
    <a class="active" style="width:160px">HOME</a>
    <a style="width:184px">ABOUT US</a>
    <a style="width:185px">SERVICES</a>
    <a style="width:206px">LOCATION</a>
    <a style="width:201px">CONTACT US</a>
  </nav>
  <div class="hero" role="img" aria-label="Sunlit pine forest"></div>

  <div class="card" style="left:24px">
    <div class="card-photo" role="img" aria-label="Stacked logs in snow" style="background:linear-gradient(135deg,#e8e6e0,#b49a78 60%,#8a7358)"></div>
    <div class="card-label">WOOD HARVESTING<span class="arrow"><svg width="12" height="12" viewBox="0 0 12 12"><path d="M4 2l4 4-4 4" stroke="#6b3510" stroke-width="2.2" fill="none"/></svg></span></div>
  </div>
  <div class="card" style="left:329px">
    <div class="card-photo" role="img" aria-label="Foresters in safety vests measuring a tree" style="background:linear-gradient(135deg,#5d7a5a,#c9c24a 50%,#e08a2a)"></div>
    <div class="card-label">FOREST MANAGEMENT<span class="arrow"><svg width="12" height="12" viewBox="0 0 12 12"><path d="M4 2l4 4-4 4" stroke="#6b3510" stroke-width="2.2" fill="none"/></svg></span></div>
  </div>
  <div class="card" style="left:632px">
    <div class="card-photo" role="img" aria-label="Close view of cut log ends" style="background:linear-gradient(135deg,#c98a4e,#8a4e25 50%,#d7a06a)"></div>
    <div class="card-label">WOOD HARVESTING<span class="arrow"><svg width="12" height="12" viewBox="0 0 12 12"><path d="M4 2l4 4-4 4" stroke="#6b3510" stroke-width="2.2" fill="none"/></svg></span></div>
  </div>

  <h2 class="section-title" style="left:25px;top:752px">Welcome To R.T. Pell Logging Company</h2>
  <div class="rule" style="left:24px;top:790px;width:206px"></div>
  <h2 class="section-title" style="left:634px;top:752px">Video</h2>
  <div class="rule" style="left:632px;top:790px;width:206px"></div>

  <div class="intro" style="top:810px">
    <p>Receive high-quality professional logging and land clearing services, from R.T. Pell Logging Company based in Pine Hollow, TX. Whether your tract is large or small, our team of experts can provide the resources and solutions you need to get the job done right. Our track record for consistency, timely service, and expertise will continue to keep us competitive in the East Texas timber industry. We pay top dollar for your pine and hardwood timber.</p>
    <p>To speak with an experienced member of staff, simply contact us 555-014-2287 at your earliest convenience.</p>
    <p>Our office hours are:7am-8pm</p>
  </div>

  <div class="video" role="img" aria-label="Video of logging crew beside an excavator in the woods">
    <svg width="54" height="54" viewBox="0 0 54 54"><circle cx="27" cy="27" r="25" fill="#e3ac42" opacity=".9"/><path d="M21 16l17 11-17 11z" fill="#5a2c0c"/></svg>
  </div>

  <footer class="footer">
    <div class="footer-links">Home<span>|</span>About Us<span>|</span>Services<span>|</span>Location<span>|</span>Contact Us</div>
    <div class="copyright">Copyright © 2014 R.T. Pell Logging Company</div>
    <div class="follow">Follow Us :<i></i><i></i><i></i><i></i></div>
  </footer>
</div>
</body>
</html>
```